Customer Dashboard Design for Email Security SaaS

Mailbrook is a commercial email spam filter offered as a SaaS product, built and operated by a small German hosting provider. It protects business email accounts against spam, phishing, scam, and viruses using a multilayer filtering pipeline that combines traditional spam detection with AI-powered classification. The product runs entirely on German infrastructure, ensuring data sovereignty for European customers.

We need a complete redesign of the customer-facing dashboard. This is the web application where paying customers manage their email filtering: view their mail log, check quarantined emails, manage allow/blocklists, configure their settings, and handle their subscription. It is the primary touchpoint between Mailbrook and its customers.

Our customers are system administrators, IT managers at small-to-medium businesses, and operators of small hosting providers. They are technically competent but not designers. They expect professional, efficient tools that respect their time. They typically manage 10–500 email accounts and check the dashboard a few times per week, with heavier use during spam incidents.

We have attached the current mockups which really need to be replaced with something good looking.

Target Market(s)

System administrators, IT managers at small-to-medium businesses, and operators of small hosting providers.

Industry/Entity Type

SaaS

Number of Pages Required

5+ page

```html
<!DOCTYPE html>
<html lang="de">
<head>
<meta charset="utf-8">
<title>Mailbrook – Übersicht</title>
<link href="https://fonts.googleapis.com/css2?family=Outfit:wght@300;400;500;600&display=swap" rel="stylesheet">
<style>
:root{
  --page:#252525;
  --card:#000000;
  --tab:#151816;
  --accent:#17c07f;
  --text:#ffffff;
  --muted:#c9cfcc;
  --nav:#b9c0bd;
  --grid:#2c2f2e;
  --search:#1f2221;
  --red:#e0406a;
  --yellow:#f5c451;
  --grey:#6b6f6d;
}
*{box-sizing:border-box;margin:0;padding:0}
html,body{width:1200px;height:875px;overflow:hidden}
body{background:var(--page);font-family:"Outfit",sans-serif;color:var(--text);position:relative}
.app{position:absolute;left:62.5px;top:62.5px;width:1075px;height:750px;border-radius:25px 25px 0 25px;
  background:linear-gradient(120deg,#000 0%,#04100b 45%,#062118 100%);overflow:hidden}
.main{position:absolute;left:118.5px;top:93.5px;width:956.5px;height:656.5px;border-radius:31px 0 0 0;
  background:radial-gradient(ellipse at 40% 30%,#0d4a31 0%,#083222 40%,#041a12 75%,#020a07 100%)}
.abs{position:absolute}
.brand{left:114px;top:97px;display:flex;align-items:center;gap:10px}
.brand-mark{width:45px;height:45px;border-radius:12px;background:#2f9d6c}
.brand-name{font-size:21px;font-weight:600;letter-spacing:-.2px}
.search{left:481px;top:98px;width:338px;height:28px;background:var(--search);border-radius:3px;
  display:flex;align-items:center;justify-content:space-between;padding:0 10px 0 14px;font-size:10.5px}
.bell{left:955px;top:103px}
.badge{left:964px;top:103px;width:9px;height:9px;border-radius:50%;background:var(--accent);font-size:6px;line-height:9px;text-align:center}
.avatar{left:987px;top:93px;width:38px;height:38px;border-radius:50%;border:2px solid var(--accent);background:radial-gradient(circle at 50% 40%,#6b5547,#2a4a3e)}
.user{left:1032px;top:104px;font-size:11px;display:flex;align-items:center;gap:10px}
.sidebar{left:94px;top:194px;width:90px}
.nav{position:absolute;left:0;width:87px;height:50px;text-align:center;font-size:8px;letter-spacing:.8px;color:var(--nav);font-weight:400}
.nav svg{display:block;margin:8px auto 4px}
.nav.active{background:#0b3b27;border-radius:25px 0 0 25px;color:var(--accent)}
.nav-bar{left:177px;top:208px;width:4px;height:22px;background:var(--accent)}
.greet{left:239px;top:198px;font-size:31px;font-weight:300}
.greet b{color:var(--accent);font-weight:500}
.mode{left:239px;top:244px;font-size:12.5px;font-weight:300;color:var(--muted)}
.card{position:absolute;top:300px;width:269px;height:175px;background:var(--card);border-radius:25px}
.card-tab{position:absolute;right:6px;top:6px;width:31px;height:31px;background:var(--tab);border-radius:0 18px 0 0;display:flex;align-items:center;justify-content:center}
.card-head{position:absolute;left:32px;top:26px;display:flex;align-items:center;gap:11px;font-size:12px;font-weight:400}
.card-head.strong{font-weight:500}
.card-num{position:absolute;left:32px;top:70px;font-size:44px;font-weight:300}
.card-sub{position:absolute;left:32px;top:134px;font-size:11.5px;font-weight:300;color:var(--muted)}
.chart{left:231px;top:500px;width:856px;height:262px;background:var(--card);border-radius:25px}
.chart-title{position:absolute;left:33px;top:26px;font-size:16px;font-weight:300}
.btn{position:absolute;left:696px;top:25px;width:129px;height:25px;border-radius:6px;background:linear-gradient(#0e9a62,#0a6f47);font-size:10px;font-weight:400;display:flex;align-items:center;justify-content:center;font-family:inherit;color:var(--text);border:0}
.gl{position:absolute;left:50px;width:775px;height:1px;background:var(--grid)}
.gv{position:absolute;font-size:9.5px;color:var(--muted);width:20px;text-align:right;left:21px}
.legend{position:absolute;left:32px;top:212px;display:flex;gap:17px;font-size:10.5px;font-weight:300;color:var(--muted)}
.legend span{display:flex;align-items:center;gap:5px}
.legend i{width:7px;height:7px;border-radius:1px;display:inline-block}
</style>
</head>
<body>
<div class="app"><div class="main"></div></div>

<div class="abs brand"><div class="brand-mark"></div><span class="brand-name">Mailbrook</span></div>

<div class="abs search"><span>Search</span>
<svg width="15" height="15" viewBox="0 0 24 24" fill="none" stroke="#fff" stroke-width="2"><circle cx="10" cy="10" r="7"/><path d="M15 15l6 6"/></svg></div>

<svg class="abs bell" width="16" height="16" viewBox="0 0 24 24" fill="none" stroke="#fff" stroke-width="1.6"><path d="M6 16V11a6 6 0 0112 0v5l2 2H4z"/><path d="M10 20a2 2 0 004 0"/></svg>
<div class="abs badge">2</div>
<div class="abs avatar" role="img" aria-label="Profilfoto des Nutzers"></div>
<div class="abs user">John Doe
<svg width="9" height="6" viewBox="0 0 10 6" fill="none" stroke="#fff" stroke-width="1.4"><path d="M1 1l4 4 4-4"/></svg></div>

<nav class="abs sidebar">
  <div class="nav active" style="top:0"><svg width="16" height="16" viewBox="0 0 24 24" fill="none" stroke="currentColor" stroke-width="1.6"><path d="M4 10l8-6 8 6v10H4z"/><path d="M10 20v-5h4v5"/></svg>ÜBERSICHT</div>
  <div class="nav" style="top:56px"><svg width="16" height="16" viewBox="0 0 24 24" fill="none" stroke="currentColor" stroke-width="1.6"><rect x="5" y="3" width="14" height="18" rx="2"/><path d="M9 8h6M9 12h6M9 16h6"/></svg>MAIL-LOG</div>
  <div class="nav" style="top:112px"><svg width="16" height="16" viewBox="0 0 24 24" fill="none" stroke="currentColor" stroke-width="1.6"><rect x="3" y="7" width="16" height="12" rx="2"/><path d="M3 9l8 5 8-5"/><circle cx="19" cy="5" r="2"/></svg>POSTFÄCHER</div>
  <div class="nav" style="top:168px"><svg width="16" height="16" viewBox="0 0 24 24" fill="none" stroke="currentColor" stroke-width="1.6"><path d="M12 3l7 3v6c0 4-3 7-7 9-4-2-7-5-7-9V6z"/><path d="M9 12l2 2 4-4"/></svg>ALLOWLIST</div>
  <div class="nav" style="top:224px"><svg width="16" height="16" viewBox="0 0 24 24" fill="none" stroke="currentColor" stroke-width="1.6"><path d="M12 3l10 18H2z"/><path d="M12 10v5M12 18v.5"/></svg>BLOCKLIST</div>
  <div class="nav" style="top:280px"><svg width="16" height="16" viewBox="0 0 24 24" fill="none" stroke="currentColor" stroke-width="1.6"><rect x="5" y="10" width="14" height="11" rx="2"/><path d="M8 10V7a4 4 0 018 0v3"/><circle cx="12" cy="15" r="1.5"/></svg>QUARANTÄNE</div>
  <div class="nav" style="top:336px"><svg width="16" height="16" viewBox="0 0 24 24" fill="none" stroke="currentColor" stroke-width="1.6"><circle cx="12" cy="12" r="3"/><path d="M12 2v3M12 19v3M2 12h3M19 12h3M5 5l2 2M17 17l2 2M5 19l2-2M17 7l2-2"/></svg>EINSTELLUNGEN</div>
  <div class="nav" style="top:392px"><svg width="16" height="16" viewBox="0 0 24 24" fill="none" stroke="currentColor" stroke-width="1.6"><path d="M6 3h9l4 4v14H6z"/><path d="M12 9v8M14 10.5c-1-1-4-1-4 .8s4 1 4 3-3 1.7-4 .8"/></svg>ABRECHNUNG</div>
</nav>
<div class="abs nav-bar"></div>

<h1 class="abs greet">Guten Tag, <b>John Doe</b></h1>
<p class="abs mode">Beobachtungsmodus - Mails werden analysiert aber nicht blockiert</p>

<section class="card" style="left:231px">
  <div class="card-tab"><svg width="14" height="10" viewBox="0 0 14 10" fill="none" stroke="#17c07f" stroke-width="1.2"><rect x=".6" y=".6" width="12.8" height="8.8" rx="1"/><path d="M1 1l6 4 6-4"/></svg></div>
  <div class="card-head strong"><svg width="30" height="30" viewBox="0 0 30 30" fill="none" stroke="#c9cfcc" stroke-width="1.5"><path d="M26 10A13 13 0 1 0 27 18"/><path d="M26 4v6h-6"/><text x="7" y="19" font-size="9" fill="#c9cfcc" stroke="none" font-family="Outfit">24h</text></svg>Letzte 24 Stunden</div>
  <div class="card-num">0</div>
  <div class="card-sub">0 zugestellt, 0 abgefangen</div>
</section>
<section class="card" style="left:525px">
  <div class="card-tab"><svg width="14" height="10" viewBox="0 0 14 10" fill="none" stroke="#17c07f" stroke-width="1.2"><rect x=".6" y=".6" width="12.8" height="8.8" rx="1"/><path d="M1 1l6 4 6-4"/></svg></div>
  <div class="card-head"><svg width="30" height="30" viewBox="0 0 30 30" fill="none" stroke="#c9cfcc" stroke-width="1.3"><rect x="1" y="4" width="28" height="25" rx="2"/><path d="M1 10h28M6 1v6M12 1v6M18 1v6M24 1v6"/><text x="12" y="24" font-size="9" fill="#c9cfcc" stroke="none" font-family="Outfit">7</text></svg>7 TAGE</div>
  <div class="card-num">0</div>
  <div class="card-sub">0 zugestellt</div>
</section>
<section class="card" style="left:819px">
  <div class="card-tab"><svg width="14" height="10" viewBox="0 0 14 10" fill="none" stroke="#17c07f" stroke-width="1.2"><rect x=".6" y=".6" width="12.8" height="8.8" rx="1"/><path d="M1 1l6 4 6-4"/></svg></div>
  <div class="card-head"><svg width="30" height="30" viewBox="0 0 30 30" fill="none" stroke="#c9cfcc" stroke-width="1.3"><rect x="1" y="4" width="28" height="25" rx="2"/><path d="M1 10h28M6 1v6M12 1v6M18 1v6M24 1v6"/><text x="9" y="24" font-size="9" fill="#c9cfcc" stroke="none" font-family="Outfit">30</text></svg>30 TAGE</div>
  <div class="card-num">0</div>
  <div class="card-sub">0 zugestellt</div>
</section>

<section class="abs chart">
  <h2 class="chart-title">Letzte 30 Tage</h2>
  <button class="btn">Datentabelle anzeigen</button>
  <div class="gv" style="top:71px">10</div><div class="gl" style="top:78px"></div>
  <div class="gv" style="top:121px">5</div><div class="gl" style="top:128px"></div>
  <div class="gv" style="top:171px">0</div><div class="gl" style="top:178px"></div>
  <div class="legend">
    <span><i style="background:var(--accent)"></i>Akzeptiert</span>
    <span><i style="background:var(--red)"></i>Abgelehnt</span>
    <span><i style="background:var(--yellow)"></i>Quarantäne</span>
    <span><i style="background:var(--grey)"></i>Tempfail</span>
  </div>
</section>
</body>
</html>
```